Fast Money - Simple Book Cover Design

Hello,

I am in need of a cover for my new book. The Book Title Is

"Standing Growth - Keys to Glowing Customer Ratings That Fill The Calendar and Draw Fresh Clients Through Every Entrance!"

Author: Fireman Dale Orsworth

What I want: This is a book for businesses on improving their online reputation. I want to have 5 Stars on the cover. You can look at this quarvex search for ideas of what I am meaning.....

(copy and paste)

http://www.quarvex-find.example/search?q=5+star+online+reviews&mode=images&ref=kx7Lp2QwZt9 (copy and paste)

I am open to different color schemes for the book. I am partial to dark blues if you make it look good. Here is another book that I really like the cover of....

http://www.brindlemart.example/Clipwave-Tactics-Earning-Promotion-ebook/item/Z93KT4WQPX

I want the cover BOLD and to STAND OUT.

I am looking for a design to help establish me as an authority for online reputation marketing. This book will be both in Pagely format and be used in print as well.

I am open to questions....

Thanks!

Dale

Reason: I don't believe we have received the right designs. I am going to give everyone more time...

Reason: Hi everyone, I had some stuff come up and was not able to be involved in this project. I am extending because we have not seen the exact thing we want and need time to work with designers to get it right. Thanks Dale

Reason: I am currently traveling and can't wrap this up until I get back.

Target Market(s)

Business Owners

Industry/Entity Type

Business

Requirements
Must have
• Title and Subtitle

Author Name

5 Stars Images....
Nice to have
• Creativity

Bold and stand out

Professional

Should not have
• thin text, small to read text, lame graphics,

```html
<!DOCTYPE html>
<html lang="en">
<head>
<meta charset="utf-8">
<title>Standing Growth – Book Cover</title>
<link href="https://fonts.googleapis.com/css2?family=Archivo+Black&family=Cinzel:wght@700&display=swap" rel="stylesheet">
<style>
  :root {
    --page-bg: #f2f3f6;
    --navy-deep: #0b1250;
    --navy: #1a2a8c;
    --royal: #2b46c8;
    --streak: rgba(120, 160, 255, 0.22);
    --streak-soft: rgba(160, 190, 255, 0.12);
    --white: #ffffff;
    --star-gold: #f7dc0c;
    --star-edge: #1b1d3c;
    --author-blue: #1c2a8f;
    --outline: #070b2e;
  }
  * { margin: 0; padding: 0; box-sizing: border-box; }
  html, body {
    width: 952px; height: 1200px; overflow: hidden;
    background: var(--page-bg);
  }
  .canvas {
    position: relative; width: 952px; height: 1200px;
  }
  .cover {
    position: absolute; left: 68px; top: 60px;
    width: 816px; height: 1080px; overflow: hidden;
    background: linear-gradient(160deg, var(--navy-deep) 0%, var(--navy) 45%, var(--royal) 75%, var(--navy-deep) 100%);
    box-shadow: 0 10px 30px rgba(0,0,0,0.25);
  }
  .cover-streaks { position: absolute; inset: 0; width: 100%; height: 100%; }
  .title {
    position: absolute; top: 36px; left: 0; right: 0;
    text-align: center;
    font-family: "Archivo Black", "Arial Black", sans-serif;
    font-size: 124px; line-height: 1.02; color: var(--white);
    -webkit-text-stroke: 3px var(--outline);
    paint-order: stroke fill;
    text-shadow: 4px 5px 0 var(--outline), 0 0 14px rgba(0,0,0,0.5);
    letter-spacing: -1px;
  }
  .rating-stars {
    position: absolute; top: 318px; left: 108px; width: 600px; height: 110px;
  }
  .subtitle {
    position: absolute; top: 470px; left: 0; right: 0;
    text-align: center;
    font-family: "Cinzel", "Times New Roman", serif;
    font-weight: 700; font-size: 46px; line-height: 1.42;
    color: var(--white);
    text-shadow: 2px 3px 4px rgba(0,0,0,0.6);
  }
  .author-band {
    position: absolute; left: 0; right: 0; top: 902px; height: 108px;
    background: var(--white);
    display: flex; align-items: center; justify-content: center;
    box-shadow: 0 -3px 10px rgba(0,0,0,0.3);
  }
  .author-name {
    font-family: "Archivo Black", "Arial Black", sans-serif;
    font-size: 54px; color: var(--author-blue); letter-spacing: -0.5px;
  }
  .base-strip {
    position: absolute; left: 0; right: 0; top: 1010px; bottom: 0;
    background: linear-gradient(180deg, var(--royal), var(--navy-deep));
  }
</style>
</head>
<body>
<div class="canvas">
  <div class="cover">
    <svg class="cover-streaks" viewBox="0 0 816 1080" preserveAspectRatio="none" aria-hidden="true">
      <polygon points="816,380 816,520 0,980 0,900" fill="var(--streak)"/>
      <polygon points="816,560 816,610 0,1060 0,1020" fill="var(--streak-soft)"/>
      <polygon points="520,0 640,0 0,720 0,600" fill="var(--streak-soft)"/>
      <polygon points="816,700 816,820 300,1080 140,1080" fill="var(--streak)"/>
    </svg>

    <h1 class="title">Standing<br>Growth</h1>

    <svg class="rating-stars" viewBox="0 0 600 110" role="img" aria-label="Five star rating">
      <defs>
        <polygon id="star" points="50,6 61,40 97,40 68,61 79,96 50,75 21,96 32,61 3,40 39,40"
                 fill="var(--star-gold)" stroke="var(--star-edge)" stroke-width="5" stroke-linejoin="round"/>
      </defs>
      <use href="#star" x="0" y="4"/>
      <use href="#star" x="125" y="4"/>
      <use href="#star" x="250" y="4"/>
      <use href="#star" x="375" y="4"/>
      <use href="#star" x="500" y="4"/>
    </svg>

    <p class="subtitle">
      Keys to Glowing Customer<br>
      Ratings That Fill The<br>
      Calendar and Draw Fresh<br>
      Clients Through Every<br>
      Entrance
    </p>

    <div class="author-band">
      <span class="author-name">Fireman Dale Orsworth</span>
    </div>
    <div class="base-strip"></div>
  </div>
</div>
</body>
</html>
```